ALL TEXT GRAPHICS TM May 2025 for Instagram

We are looking for a series of social media graphics for Instagram (new size: 4:5 (1080 x 1350 pixels) ratio that are ALL TEXT. We want the following quotes below on each graphic; one quote per graphic. AND, In very small letters at the bottom of each graphic, add @TovaMarshOnline
The look and feel of these graphics should be complimentary to the color palette attached below; but keep them simple. But the design is up to you; at the end of this document, I provided various samples of all text graphics that I like as examples.
Target Market(s)
women looking to lose weight
Look and feel

```html
<!DOCTYPE html>
<html lang="en">
<head>
<meta charset="utf-8">
<title>All Text Graphics – Instagram Series</title>
<link rel="stylesheet" href="https://fonts.googleapis.com/css2?family=Oswald:wght@700&family=Mulish:wght@300&display=swap">
<style>
  :root {
    --board: #b2b3b7;
    --card: #ffffff;
    --magenta: #cc0066;
    --ink: #1a1a1a;
  }
  * { margin: 0; padding: 0; box-sizing: border-box; }
  html, body {
    width: 774px;
    height: 1200px;
    overflow: hidden;
    background: var(--board);
  }
  .series {
    position: relative;
    width: 774px;
    height: 1200px;
    display: grid;
    grid-template-columns: repeat(3, 210px);
    grid-auto-rows: 263px;
    column-gap: 24px;
    row-gap: 18px;
    padding: 45px 0 0 43px;
  }
  .post {
    position: relative;
    background: var(--card);
    padding: 24px 14px 0 17px;
    display: flex;
    flex-direction: column;
  }
  .post::after {
    content: "";
    position: absolute;
    left: 0; right: 0; bottom: 0;
    height: 12px;
    background: var(--magenta);
  }
  .post__headline {
    font-family: "Oswald", sans-serif;
    font-weight: 700;
    font-size: 23.5px;
    line-height: 28.5px;
    text-transform: uppercase;
    color: var(--magenta);
  }
  .post__body {
    font-family: "Mulish", sans-serif;
    font-weight: 300;
    font-size: 17.5px;
    line-height: 22.5px;
    color: var(--ink);
    margin-top: 8px;
  }
  .post__handle {
    font-family: "Oswald", sans-serif;
    font-weight: 700;
    font-size: 5px;
    text-transform: uppercase;
    color: var(--magenta);
    margin-top: 14px;
    margin-left: 2px;
  }
  .post--tight .post__headline { font-size: 23px; }
</style>
</head>
<body>
<main class="series">
  <article class="post">
    <h2 class="post__headline">Bloating.<br>Muffin top.<br>Puffy waistline.</h2>
    <p class="post__body">Your body’s<br>screaming for<br>a different kind<br>of fix.</p>
    <p class="post__handle">@TovaMarshOnline</p>
  </article>
  <article class="post">
    <h2 class="post__headline">That stubborn<br>weight? It’s not<br>your fault.</h2>
    <p class="post__body">Your hormones are to blame and you’re not alone; But there is a fix.</p>
    <p class="post__handle">@TovaMarshOnline</p>
  </article>
  <article class="post" style="padding-top:12px">
    <h2 class="post__headline">Your belly<br>isn’t fat… it’s<br>hormonal. And<br>here’s how to<br>fix it.</h2>
    <p class="post__body" style="margin-top:4px">Comment<br>HORMONES if<br>nothing is working.</p>
    <p class="post__handle">@TovaMarshOnline</p>
  </article>

  <article class="post">
    <h2 class="post__headline">The stubborn<br>belly fat after<br>40?</h2>
    <p class="post__body">It’s not about calories; it’s about your hormones. Here is the fix!</p>
    <p class="post__handle" style="margin-top:18px">@TovaMarshOnline</p>
  </article>
  <article class="post" style="padding-top:28px">
    <h2 class="post__headline">Flat tummy in<br>your 40s?</h2>
    <p class="post__body">It’s still possible! Comment BYE BELLY to get the 10 secrets to a flatter tummy</p>
    <p class="post__handle" style="margin-top:18px">@TovaMarshOnline</p>
  </article>
  <article class="post">
    <h2 class="post__headline">Bloating.<br>Muffin top.<br>Puffy waistline.</h2>
    <p class="post__body">Your body’s screaming for a different kind of fix. Here it is</p>
    <p class="post__handle" style="margin-top:18px">@TovaMarshOnline</p>
  </article>

  <article class="post">
    <h2 class="post__headline">You’re doing all the “right” things, but your belly won’t go down?</h2>
    <p class="post__body" style="margin-top:2px">Here’s what you<br>haven’t tried.</p>
    <p class="post__handle">@TovaMarshOnline</p>
  </article>
  <article class="post" style="padding-top:16px">
    <h2 class="post__headline">This 90-day plan<br>helped women<br>over 40 slim<br>down, get a tiny<br>waist and feel<br>sexy again.</h2>
    <p class="post__body" style="margin-top:0">You’re next.</p>
    <p class="post__handle">@TovaMarshOnline</p>
  </article>
  <article class="post" style="padding-top:12px;padding-left:9px;padding-right:4px">
    <h2 class="post__headline">This is the secret women over 40 are using to get snatched; without starving.</h2>
    <p class="post__body" style="margin-top:6px">Comment SKINNY to get the exact plan.</p>
    <p class="post__handle" style="margin-left:3px">@TovaMarshOnline</p>
  </article>

  <article class="post">
    <h2 class="post__headline">What worked in<br>your 30s won’t<br>work now.</h2>
    <p class="post__body">Here’s what<br>actually does.<br>Drop 30 Pounds<br>in 3 Months.</p>
    <p class="post__handle" style="margin-top:18px">@TovaMarshOnline</p>
  </article>
</main>
</body>
</html>
```